Medical Diagnoses Illustration

I will provide a list of diagnoses for neck conditions. I would like the illustrator to fit each diagnosis in to the silhouette of a neck/shoulders, using separate and unique fonts/sizes for each diagnosis. The intent is to hang this illustration as a poster in a medical office, framed, as an interesting piece of art / education. This is a simple illustration, but once I find the right design, there are up to 8 more of the same type of projects that I would like done. If you can find a way to economically create the right illustration, there could be a good bit more of this work.
Updates

Now that there has been one great submission, this project has been upgraded to guaranteed payment.  Please read the feedback comments and get your designs in before the deadline.

Reason: Project extended due to Christmas.

Target Market(s)

Patients, sitting in an examination room, waiting to be examined. The clinic is upscale, with private rooms that use lots of bold, but earthy colours and a warm brown flooring. A single tone to the project would work best.

Industry/Entity Type

Medical

Requirements
Must have
• The background should be a light earthy colour, and the illustration should be single-tone, in a muted forest green, or a similar toned blue. Poster size is 11 x 14". The text can follow curvatures, but should be readable without having to crane the neck sideways.
• The illustration should be centred with the following heading above: "Know your diagnosis?" and then under the illustration "Your physiotherapist can help." Use the same colour as for the illustration, or a variation of it if you think that might look better.
Nice to have
• Try not to draw an outline of the head and neck - see if you can make the words form the silhouette. Perhaps a very light opaque outline could be placed behind the text to further define the shape of a neck/shoulders. See my examples attached.

```html
<!DOCTYPE html>
<html lang="en">
<head>
<meta charset="utf-8">
<title>Know Your Diagnosis – Neck Conditions Poster</title>
<link rel="stylesheet" href="https://fonts.googleapis.com/css2?family=Anton&family=Arimo&family=Bebas+Neue&family=Bowlby+One&family=Fredoka:wght@600&family=Great+Vibes&family=Grenze+Gotisch:wght@700&family=IM+Fell+English:ital@1&family=League+Gothic&family=Libre+Baskerville:ital,wght@1,700&family=Old+Standard+TT:wght@700&family=Oleo+Script&family=Oswald:wght@700&family=Patrick+Hand&family=Pirata+One&family=Playfair+Display:ital,wght@1,700&family=Roboto+Slab:wght@900&family=UnifrakturMaguntia&family=Yanone+Kaffeesatz:wght@500&display=swap">
<style>
  :root {
    --paper: #ffffff;
    --headline-blue: #1b74ba;
    --ink: #141414;
    --outline-fill: #ffffff;
    --silhouette-warm: #f3d6cf;
    --silhouette-light: #fdf6f4;
  }
  html, body {
    margin: 0;
    padding: 0;
    width: 1200px;
    height: 1200px;
    overflow: hidden;
    background: var(--paper);
  }
  .poster {
    display: block;
    width: 1200px;
    height: 1200px;
  }
  .silhouette-light { stop-color: var(--silhouette-light); }
  .silhouette-warm { stop-color: var(--silhouette-warm); }

  .headline, .tagline {
    font-family: "Anton", "Impact", sans-serif;
    fill: var(--headline-blue);
  }
  .headline { font-size: 150px; }
  .tagline { font-size: 92px; }

  .dx { fill: var(--ink); }
  .dx-myelopathy { font-family: "Playfair Display", serif; font-style: italic; font-weight: 700; font-size: 50px; }
  .dx-kyphosis { font-family: "Oswald", sans-serif; font-weight: 700; font-size: 66px; }
  .dx-disk-disease { font-family: "Bowlby One", sans-serif; font-size: 56px; }
  .dx-scoliosis { font-family: "Arimo", sans-serif; font-size: 48px; }
  .dx-torticollis { font-family: "Libre Baskerville", serif; font-style: italic; font-weight: 700; font-size: 52px; }
  .dx-wry-neck { font-family: "Patrick Hand", cursive; font-size: 58px; }
  .dx-cervical { font-family: "Oleo Script", cursive; font-size: 72px; }
  .dx-dystonia { font-family: "League Gothic", sans-serif; font-size: 150px; }
  .dx-lordosis { font-family: "Pirata One", serif; font-size: 120px; }
  .dx-lateral-stenosis { font-family: "Yanone Kaffeesatz", sans-serif; font-weight: 500; font-size: 78px; }
  .dx-radiculopathy { font-family: "Roboto Slab", serif; font-weight: 900; font-size: 82px; }
  .dx-disc-herniation {
    font-family: "Bebas Neue", sans-serif; font-size: 140px;
    fill: var(--outline-fill); stroke: var(--ink); stroke-width: 3px;
    paint-order: stroke; filter: drop-shadow(5px 4px 0 var(--ink));
  }
  .dx-whiplash { font-family: "Great Vibes", cursive; font-size: 78px; }
  .dx-chiari { font-family: "Grenze Gotisch", serif; font-weight: 700; font-size: 104px; }
  .dx-malformation { font-family: "Old Standard TT", serif; font-weight: 700; font-size: 96px; }
  .dx-occipital { font-family: "UnifrakturMaguntia", serif; font-size: 58px; }
  .dx-osteoarthritis {
    font-family: "Oswald", sans-serif; font-weight: 700; font-size: 70px;
    fill: var(--outline-fill); stroke: var(--ink); stroke-width: 2.5px;
    paint-order: stroke; filter: drop-shadow(4px 3px 0 var(--ink));
  }
  .dx-rheumatoid { font-family: "IM Fell English", serif; font-style: italic; font-size: 52px; }
  .dx-craniovertebral {
    font-family: "Fredoka", sans-serif; font-weight: 600; font-size: 72px;
    fill: var(--outline-fill); stroke: var(--ink); stroke-width: 3px;
    paint-order: stroke; filter: drop-shadow(4px 4px 0 var(--ink));
  }
</style>
</head>
<body>
<svg class="poster" viewBox="0 0 1200 1200" xmlns="http://www.w3.org/2000/svg" role="img" aria-labelledby="poster-title">
  <title id="poster-title">Know Your Diagnosis – neck condition names forming a neck and shoulders silhouette. Your physiotherapist can help.</title>
  <defs>
    <linearGradient id="silhouette-fill" x1="0" y1="1" x2="1" y2="0">
      <stop offset="0" class="silhouette-warm"/>
      <stop offset="0.75" class="silhouette-light"/>
    </linearGradient>
    <path id="disk-disease-curve" d="M92 442 C200 400 330 388 420 386 C478 382 525 320 575 225"/>
  </defs>

  <text class="headline" x="82" y="140" textLength="1040" lengthAdjust="spacingAndGlyphs">Know Your Diagnosis</text>

  <path class="neck-silhouette" fill="url(#silhouette-fill)"
        d="M477 150 L705 150 L705 290 Q720 332 900 345 L1080 360 Q1132 378 1136 432 L1140 1022 L82 1022 L88 425 Q92 372 150 362 Q420 332 472 292 Z"/>

  <g class="diagnoses">
    <text class="dx dx-myelopathy" x="518" y="205" textLength="187" lengthAdjust="spacingAndGlyphs">Myelopathy</text>
    <text class="dx dx-kyphosis" x="570" y="277" textLength="142" lengthAdjust="spacingAndGlyphs">Kyphosis</text>
    <text class="dx dx-disk-disease"><textPath href="#disk-disease-curve" textLength="540" lengthAdjust="spacingAndGlyphs">DISK Disease</textPath></text>
    <text class="dx dx-scoliosis" x="535" y="360" textLength="155" lengthAdjust="spacingAndGlyphs">Scoliosis</text>
    <text class="dx dx-torticollis" x="712" y="362" textLength="192" lengthAdjust="spacingAndGlyphs" transform="rotate(11 712 362)">Torticollis</text>
    <text class="dx dx-wry-neck" x="915" y="405" textLength="212" lengthAdjust="spacingAndGlyphs" transform="rotate(14 915 405)">(wry neck)</text>
    <text class="dx dx-cervical" x="90" y="512" textLength="195" lengthAdjust="spacingAndGlyphs">Cervical</text>
    <text class="dx dx-dystonia" x="290" y="500" textLength="205" lengthAdjust="spacingAndGlyphs" transform="skewX(-10) translate(88 0)">Dystonia</text>
    <text class="dx dx-lordosis" x="532" y="498" textLength="225" lengthAdjust="spacingAndGlyphs">Lordosis</text>
    <text class="dx dx-lateral-stenosis" x="775" y="495" textLength="348" lengthAdjust="spacingAndGlyphs" transform="rotate(7.5 775 495)">Lateral Stenosis</text>
    <text class="dx dx-radiculopathy" x="93" y="620" textLength="455" lengthAdjust="spacingAndGlyphs">Radiculopathy</text>
    <text class="dx dx-disc-herniation" x="585" y="638" textLength="532" lengthAdjust="spacingAndGlyphs">DISC HERNIATION</text>
    <text class="dx dx-whiplash" x="93" y="718" textLength="1025" lengthAdjust="spacingAndGlyphs">Whiplash Associated Disorder</text>
    <text class="dx dx-chiari" x="93" y="824" textLength="355" lengthAdjust="spacingAndGlyphs">Chiari</text>
    <text class="dx dx-malformation" x="442" y="822" textLength="676" lengthAdjust="spacingAndGlyphs">Malformation</text>
    <text class="dx dx-occipital" x="510" y="868" textLength="608" lengthAdjust="spacingAndGlyphs">Occipital Neuralgia</text>
    <text class="dx dx-osteoarthritis" x="93" y="910" textLength="368" lengthAdjust="spacingAndGlyphs">OSTEOARTHRITIS</text>
    <text class="dx dx-rheumatoid" x="495" y="920" textLength="623" lengthAdjust="spacingAndGlyphs">Rheumatoid Arthritis</text>
    <text class="dx dx-craniovertebral" x="90" y="992" textLength="1028" lengthAdjust="spacingAndGlyphs">Craniovertebral instability</text>
  </g>

  <text class="tagline" x="75" y="1165" textLength="1045" lengthAdjust="spacingAndGlyphs">Your physiotherapist can help</text>
</svg>
</body>
</html>
```